Stationary Set Rebrand for Brenvik

We are a Canadian Distribution and Service Company that was established in 1969. Over the past 5 decades we have expanded our business and have warehouses across Canada. We specialize in adhesive tapes, adhesives, films, safety, warehouse, shipping, janitorial and packaging supplies.

We have updated our logo design and would like a new corporate branding identity that includes a new fresh Stationary Set (Business Cards, Letterhead, Letterhead MS Word, Envelope, Presentation Folders, Email Signatures, Notepad Covers, etc.)

Target Market(s)

Industrial Business Sector

Font styles to use
Sans Serif

Colors
0054AA
0677BA
7BADD7
CADEEF
E8F1F8
0094D4
00A9DD
6FCCEA
C7EBF8
E9F6FB
00AB8E
00BBA5
67D7C9
C6EFE9
E9F9F6
EB3D1F
EC4F4E
F09395
F8D3D4
FCEDEE

Requirements
Should not have
• Colors not too light, darker colours preferred

```html
<!DOCTYPE html>
<html lang="en">
<head>
<meta charset="utf-8">
<title>Brenvik Stationery Set</title>
<link href="https://fonts.googleapis.com/css2?family=Montserrat:wght@400;500;600;700&family=Oswald:wght@500&display=swap" rel="stylesheet">
<style>
  :root{
    --ink:#231f20;
    --ink-soft:#2e2a2b;
    --red:#e42524;
    --paper:#ffffff;
    --stage:#dcdde0;
    --stage-low:#e9e9eb;
    --leaf-light:#efefef;
    --leaf-dark:#302c2d;
    --text:#3a3a3a;
    --muted:#8a8a8a;
    --rule:#c9c9c9;
  }
  *{box-sizing:border-box;margin:0;padding:0}
  html,body{width:1039px;height:1200px;overflow:hidden}
  body{background:var(--stage);font-family:"Montserrat",sans-serif;color:var(--text);position:relative}
  .piece{position:absolute;box-shadow:0 3px 6px rgba(0,0,0,.28)}
  .wordmark{display:inline-block;line-height:1}
  .wordmark-name{display:block;font-weight:700;letter-spacing:-.02em;font-size:var(--s,20px)}
  .wordmark-tag{display:block;font-weight:500;font-size:calc(var(--s,20px)*.26);letter-spacing:.01em;margin-top:.1em}
  .on-dark{color:var(--paper)}
  .on-light{color:var(--ink)}
  .leaf{position:absolute;background:radial-gradient(circle at 50% 45%,var(--leaf-light) 55%,transparent 72%)}
  .leaf.dark{background:radial-gradient(circle at 50% 45%,var(--leaf-dark) 55%,transparent 72%)}
  .contact{list-style:none}
  .contact li{display:flex;align-items:center;gap:.35em;white-space:nowrap}
  .contact svg{width:.85em;height:.85em;flex:none;fill:var(--red)}
  .red{color:var(--red)}

  /* business card front */
  .card-front{left:61px;top:78px;width:268px;height:157px;background:var(--ink);border-radius:7px}
  .card-front .wordmark{position:absolute;left:23px;top:63px;--s:30px}
  .card-front .divider{position:absolute;left:142px;top:38px;width:1px;height:81px;background:var(--red)}
  .card-front .details{position:absolute;left:154px;top:36px;color:var(--paper);font-size:7.3px;line-height:10.5px}
  .card-front .person{font-size:10px;font-weight:600;line-height:12px}
  .card-front .role{font-size:7px;line-height:10px;margin-bottom:4px}

  /* business card back */
  .card-back{left:61px;top:273px;width:268px;height:157px;border-radius:7px;overflow:hidden}
  .card-back .pattern{position:absolute;inset:0;background:linear-gradient(135deg,#2c2c2e,#1b1b1c 60%,#262527)}
  .card-back .wordmark{position:absolute;left:46px;top:52px;--s:42px}

  /* letterhead */
  .letterhead{left:347px;top:77px;width:249px;height:353px;background:var(--paper);overflow:hidden}
  .letterhead .wordmark{position:absolute;left:21px;top:19px;--s:18px}
  .letterhead .head-contact{position:absolute;left:170px;top:14px;padding-left:4px;border-left:.6px solid var(--red);font-size:4.3px;line-height:6.3px;color:var(--ink)}
  .letterhead .double-rule{position:absolute;left:21px;top:54px;width:206px;height:3px;border-top:.6px solid var(--ink);border-bottom:.6px solid var(--ink)}
  .letterhead .recipient{position:absolute;left:21px;top:80px;font-size:4.6px;font-weight:600;color:var(--ink);line-height:6px}
  .letterhead .recipient small{display:block;font-size:3.4px;font-weight:500}
  .letterhead .date{position:absolute;right:22px;top:85px;font-size:3.4px;color:var(--muted)}
  .letterhead .body{position:absolute;left:21px;top:105px;width:206px;font-size:3.3px;line-height:6px;color:var(--muted);text-align:justify}
  .letterhead .body p+p{margin-top:6px}
  .letterhead .signature{position:absolute;left:21px;top:318px;width:54px;height:14px;background:linear-gradient(90deg,#f3f3f3,#fafafa)}
  .letterhead .signer{position:absolute;left:21px;top:262px;font-size:4.6px;font-weight:600;color:var(--ink);line-height:6px}
  .letterhead .signer small{display:block;font-size:3.4px;font-weight:500}
  .letterhead .leaf{left:135px;top:230px;width:120px;height:125px}

  /* envelope */
  .envelope-back{left:619px;top:77px;width:356px;height:172px;background:var(--paper);overflow:hidden}
  .envelope-back svg.flap{position:absolute;left:0;top:0;width:356px;height:64px}
  .envelope-back .wordmark{position:absolute;left:142px;top:19px;--s:17px}
  .envelope-front{left:619px;top:259px;width:356px;height:171px;background:var(--paper);overflow:hidden}
  .envelope-front .wordmark{position:absolute;left:17px;top:15px;--s:20px}
  .envelope-front .return{position:absolute;left:17px;top:41px;font-size:5px;line-height:7px;color:var(--ink)}
  .envelope-front .leaf{left:225px;top:40px;width:125px;height:135px}

  /* small card */
  .card-white{left:70px;top:500px;width:251px;height:75px;background:var(--paper)}
  .card-white .person{position:absolute;left:13px;top:11px;font-size:8.5px;font-weight:600;color:var(--ink);line-height:10px}
  .card-white .role{position:absolute;left:13px;top:21px;font-size:6.5px}
  .card-white .contact{position:absolute;left:13px;top:39px;font-size:6.6px;line-height:9.5px;color:var(--ink)}
  .card-white .wordmark{position:absolute;right:14px;top:10px;--s:19px;text-align:right}
  .card-white .address{position:absolute;right:17px;top:50px;font-size:6.4px;line-height:9.5px;text-align:right;color:var(--ink)}

  /* compliments slip */
  .compliments{left:61px;top:604px;width:278px;height:143px;background:var(--paper);overflow:hidden}
  .compliments .wordmark{position:absolute;left:14px;top:14px;--s:18px}
  .compliments .title{position:absolute;right:14px;top:16px;font-family:"Oswald",sans-serif;font-weight:500;font-size:12.5px;color:var(--red)}
  .compliments .leaf{left:185px;top:45px;width:100px;height:105px}
  .compliments .contact{position:absolute;left:14px;top:82px;font-size:5.5px;line-height:8.5px;color:var(--ink)}

  /* notebook cover */
  .notebook{left:360px;top:493px;width:203px;height:274px}
  .notebook .spiral{position:absolute;left:0;top:6px;width:20px;height:262px;background:repeating-linear-gradient(180deg,#9c9c9c 0 1.6px,#dcdcdc 1.6px 2.6px,transparent 2.6px 4.4px)}
  .notebook .cover{position:absolute;left:10px;top:0;width:193px;height:274px;background:var(--ink);box-shadow:0 3px 6px rgba(0,0,0,.3)}
  .notebook .wordmark{position:absolute;left:42px;top:120px;--s:29px}

  /* open notebook */
  .notebook-open{left:589px;top:491px;width:390px;height:274px;background:var(--paper)}
  .notebook-open .page{position:absolute;top:0;width:180px;height:274px}
  .notebook-open .page.left{left:4px}
  .notebook-open .page.right{left:200px}
  .notebook-open .wordmark{position:absolute;left:14px;top:14px;--s:13px}
  .notebook-open .date{position:absolute;right:10px;top:35px;font-size:3.4px;color:var(--muted)}
  .notebook-open .lines{position:absolute;left:14px;right:8px;top:45px;height:200px;background:repeating-linear-gradient(180deg,transparent 0 10.2px,var(--rule) 10.2px 11px)}
  .notebook-open .binding{position:absolute;left:183px;top:6px;width:22px;height:262px;background:repeating-linear-gradient(180deg,#8d8d8d 0 2px,#e0e0e0 2px 3.4px,transparent 3.4px 11.9px)}

  /* folders */
  .folder-stage{position:absolute;left:0;top:818px;width:1039px;height:382px;background:var(--stage-low)}
  .folder-outside{left:40px;top:866px;width:440px;height:292px;background:var(--ink);overflow:hidden}
  .folder-outside .spine{position:absolute;left:219px;top:0;width:2px;height:100%;background:var(--ink-soft)}
  .folder-outside .leaf{left:60px;top:60px;width:230px;height:240px}
  .folder-outside .front-mark{position:absolute;left:300px;top:30px;--s:22px}
  .folder-outside .web{position:absolute;right:20px;bottom:22px;font-size:6px;color:var(--paper)}
  .folder-outside .back-mark{position:absolute;left:22px;top:196px;--s:18px}
  .folder-outside .back-rule{position:absolute;left:22px;top:226px;width:150px;height:.6px;background:var(--red)}
  .folder-outside .back-contact{position:absolute;left:22px;top:233px;font-size:5.2px;line-height:8px;color:var(--paper)}
  .folder-outside .back-contact .row{display:flex;gap:8px}

  .folder-inside{left:559px;top:866px;width:440px;height:292px;background:var(--paper);overflow:hidden}
  .folder-inside .fold{position:absolute;left:219px;top:0;width:2px;height:100%;background:#d8d8d8}
  .folder-inside .pocket{position:absolute;top:186px;width:219px;height:106px;background:var(--ink)}
  .folder-inside .pocket.left{left:0;border-top-right-radius:14px}
  .folder-inside .pocket.right{left:221px;border-top-left-radius:14px}
  .folder-inside .pocket .wordmark{position:absolute;left:62px;top:40px;--s:22px}
  .folder-inside .slot-card{position:absolute;left:86px;top:-18px;width:80px;height:46px;background:var(--paper);box-shadow:0 1px 3px rgba(0,0,0,.3);padding:5px 6px}
  .folder-inside .slot-card .wordmark{position:static;--s:9px}
  .folder-inside .slot-card p{font-size:3px;line-height:4.2px;color:var(--ink);margin-top:3px}
</style>
</head>
<body>
<svg width="0" height="0" style="position:absolute" aria-hidden="true">
  <defs>
    <symbol id="icon-phone" viewBox="0 0 16 16"><path d="M3.6 1.5l2.3 2.4-1.3 1.8c.8 2 2.3 3.6 4.3 4.4l1.8-1.3 2.4 2.3-1.5 2.4C6.9 13.2 2.8 9.1 1.2 3z"/></symbol>
    <symbol id="icon-mail" viewBox="0 0 16 16"><path d="M1 3.5h14v9H1z M1.6 4.1L8 9l6.4-4.9" /></symbol>
    <symbol id="icon-globe" viewBox="0 0 16 16"><circle cx="8" cy="8" r="6.8"/></symbol>
  </defs>
</svg>

<!-- business card front -->
<section class="piece card-front">
  <div class="wordmark on-dark"><span class="wordmark-name">Brenvik</span><span class="wordmark-tag">Tape and Packaging Specialists</span></div>
  <div class="divider"></div>
  <div class="details">
    <p class="person">Marcus Delaney</p>
    <p class="role red">Founder &amp; CEO</p>
    <p>27-310 Birchwood Ave</p>
    <p style="margin-bottom:3px">Guelph, ON N1K 4T2</p>
    <ul class="contact">
      <li><svg><use href="#icon-phone"/></svg>519-555-0173</li>
      <li><svg><use href="#icon-mail"/></svg>info@brenviksales.com</li>
      <li><svg><use href="#icon-globe"/></svg>www.brenviksales.com</li>
    </ul>
  </div>
</section>

<!-- business card back -->
<section class="piece card-back">
  <div class="pattern" role="img" aria-label="Tonal leaf pattern"></div>
  <div class="wordmark on-dark"><span class="wordmark-name">Brenvik</span><span class="wordmark-tag">Tape and Packaging Specialists</span></div>
</section>

<!-- letterhead -->
<section class="piece letterhead">
  <div class="wordmark on-light"><span class="wordmark-name">Brenvik</span><span class="wordmark-tag">Tape and Packaging Specialists</span></div>
  <div class="head-contact">
    <p>27-310 Birchwood Ave</p>
    <p>Guelph, ON N1K 4T2</p>
    <ul class="contact">
      <li><svg><use href="#icon-phone"/></svg>519-555-0173</li>
      <li><svg><use href="#icon-mail"/></svg>info@brenviksales.com</li>
      <li><svg><use href="#icon-globe"/></svg>www.brenviksales.com</li>
    </ul>
  </div>
  <div class="double-rule"></div>
  <p class="recipient">Dear. Mrs Clara Ann Whitfield<small>Chief Director</small></p>
  <p class="date">Date: 16-October-2025</p>
  <div class="body">
    <p>We thank you for your recent enquiry regarding our industrial tape and packaging supply programs. Our team has reviewed your requirements and prepared a proposal covering adhesive tapes, stretch films, safety products and warehouse supplies. Each item can be shipped from our regional warehouses across Canada with reliable lead times and dedicated account support for your operation.</p>
    <p>Pricing is attached for standard and custom printed tapes, along with janitorial and shipping products. Volume discounts apply to recurring orders, and our service technicians are available to assess your packaging line and recommend equipment that reduces waste and downtime.</p>
    <p>Please contact us with any questions. We look forward to working with you and supporting your business for years to come.</p>
  </div>
  <div class="signature" role="img" aria-label="Handwritten signature" style="top:241px"></div>
  <p class="signer">Daniel Owen Price<small>Chief Director</small></p>
  <div class="leaf" role="img" aria-label="Faint leaf decoration"></div>
</section>

<!-- envelope back -->
<section class="piece envelope-back">
  <svg class="flap" viewBox="0 0 356 64" preserveAspectRatio="none" aria-hidden="true">
    <path d="M0 0H356L345 20Q338 34 320 36L192 56Q178 64 164 56L36 36Q18 34 11 20Z" fill="#231f20"/>
  </svg>
  <div class="wordmark on-dark"><span class="wordmark-name">Brenvik</span><span class="wordmark-tag">Tape and Packaging Specialists</span></div>
</section>

<!-- envelope front -->
<section class="piece envelope-front">
  <div class="wordmark on-light"><span class="wordmark-name">Brenvik</span><span class="wordmark-tag">Tape and Packaging Specialists</span></div>
  <p class="return">27-310 Birchwood Ave<br>Guelph, ON N1K 4T2</p>
  <div class="leaf" role="img" aria-label="Faint leaf decoration"></div>
</section>

<!-- white business card -->
<section class="piece card-white">
  <p class="person">MARCUS DELANEY</p>
  <p class="role red">Founder &amp; CEO</p>
  <ul class="contact">
    <li><svg><use href="#icon-phone"/></svg>519-555-0173</li>
    <li><svg><use href="#icon-mail"/></svg>info@brenviksales.com</li>
    <li><svg><use href="#icon-globe"/></svg>www.brenviksales.com</li>
  </ul>
  <div class="wordmark on-light"><span class="wordmark-name">Brenvik</span><span class="wordmark-tag">Tape and Packaging Specialists</span></div>
  <p class="address">27-310 Birchwood Ave<br>Guelph, ON N1K 4T2</p>
</section>

<!-- compliments slip -->
<section class="piece compliments">
  <div class="wordmark on-light"><span class="wordmark-name">Brenvik</span><span class="wordmark-tag">Tape and Packaging Specialists</span></div>
  <p class="title">With Compliments</p>
  <div class="leaf" role="img" aria-label="Faint leaf decoration"></div>
  <ul class="contact">
    <li>27-310 Birchwood Ave</li>
    <li>Guelph, ON N1K 4T2</li>
    <li><svg><use href="#icon-phone"/></svg>519-555-0173</li>
    <li><svg><use href="#icon-mail"/></svg>info@brenviksales.com</li>
    <li><svg><use href="#icon-globe"/></svg>www.brenviksales.com</li>
  </ul>
</section>

<!-- notebook cover -->
<section class="notebook" style="position:absolute">
  <div class="spiral"></div>
  <div class="cover">
    <div class="wordmark on-dark"><span class="wordmark-name">Brenvik</span><span class="wordmark-tag">Tape and Packaging Specialists</span></div>
  </div>
</section>

<!-- open notebook -->
<section class="piece notebook-open">
  <div class="page left">
    <div class="wordmark on-light"><span class="wordmark-name">Brenvik</span><span class="wordmark-tag">Tape and Packaging Specialists</span></div>
    <p class="date">Date:......./......./.........</p>
    <div class="lines"></div>
  </div>
  <div class="binding"></div>
  <div class="page right">
    <div class="wordmark on-light"><span class="wordmark-name">Brenvik</span><span class="wordmark-tag">Tape and Packaging Specialists</span></div>
    <p class="date">Date:......./......./.........</p>
    <div class="lines"></div>
  </div>
</section>

<!-- folders -->
<div class="folder-stage"></div>

<section class="piece folder-outside">
  <div class="leaf dark" role="img" aria-label="Tonal leaf decoration"></div>
  <div class="spine"></div>
  <div class="wordmark on-dark front-mark"><span class="wordmark-name">Brenvik</span><span class="wordmark-tag">Tape and Packaging Specialists</span></div>
  <p class="web">www.<span class="red">brenviksales</span>.com</p>
  <div class="wordmark on-dark back-mark"><span class="wordmark-name">Brenvik</span><span class="wordmark-tag">Tape and Packaging Specialists</span></div>
  <div class="back-rule"></div>
  <div class="back-contact">
    <p>27-310 Birchwood Ave, Guelph, ON N1K 4T2</p>
    <ul class="contact row">
      <li><svg><use href="#icon-phone"/></svg>519-555-0173</li>
      <li><svg><use href="#icon-mail"/></svg>info@brenviksales.com</li>
      <li><svg><use href="#icon-globe"/></svg>www.brenviksales.com</li>
    </ul>
  </div>
</section>

<section class="piece folder-inside">
  <div class="fold"></div>
  <div class="pocket left">
    <div class="wordmark on-dark"><span class="wordmark-name">Brenvik</span><span class="wordmark-tag">Tape and Packaging Specialists</span></div>
  </div>
  <div class="pocket right">
    <div class="slot-card">
      <div class="wordmark on-light"><span class="wordmark-name">Brenvik</span><span class="wordmark-tag">Tape and Packaging Specialists</span></div>
      <p><strong>MARCUS DELANEY</strong> <span class="red">Founder &amp; CEO</span><br>519-555-0173 · info@brenviksales.com<br>27-310 Birchwood Ave, Guelph, ON N1K 4T2</p>
    </div>
  </div>
</section>
</body>
</html>
```